Web design required

1-We need a web design for existing company based in New Zealand
2-We build residential house and light commercial
3-We has in-house designer which allow us can provide interior design
4-We modeling project before site construction, which enable both client and construction team to visually analysis whole project,

Target Market(s)

middle class residential house market
Ref: http://www.brambleworthbuilders.co.nz/

Industry/Entity Type

Construction Company

Number of Pages Required

1 page

Font styles to use
Sans Serif
Other font styles liked:
• Such as : Central Gothic or similar which has more design taste

Colors

Designer to choose colors to be used in the design.

Requirements
Must have
• Front sheet, contact information, sample project

```html
<!DOCTYPE html>
<html lang="en">
<head>
<meta charset="utf-8">
<title>Harwood Homes</title>
<link rel="stylesheet" href="https://fonts.googleapis.com/css2?family=Didact+Gothic&family=Open+Sans:ital,wght@0,400;0,600;0,700;1,400&display=swap">
<style>
  :root {
    --brand-blue: #0f57a8;
    --brand-blue-deep: #0b4a93;
    --ink: #333333;
    --ink-soft: #555555;
    --nav-ink: #444444;
    --white: #ffffff;
    --hero-dark: #2a2f36;
  }
  * { margin: 0; padding: 0; box-sizing: border-box; }
  html, body { width: 1200px; height: 2466px; overflow: hidden; background: var(--white); }
  body { position: relative; font-family: "Didact Gothic", "Century Gothic", sans-serif; color: var(--ink); }

  .site-header { position: absolute; top: 0; left: 0; width: 1200px; height: 79px; background: var(--white); border-top: 4px solid var(--brand-blue); }
  .brand { position: absolute; left: 164px; top: 20px; display: flex; align-items: center; gap: 12px; }
  .brand-mark { width: 30px; height: 30px; background: var(--brand-blue); }
  .brand-name { font-size: 25px; color: var(--ink-soft); letter-spacing: 0.5px; }
  .main-nav a { position: absolute; top: 32px; font-size: 12.5px; letter-spacing: 1.2px; color: var(--nav-ink); text-decoration: none; font-family: "Open Sans", sans-serif; }
  .main-nav a.is-active { color: var(--brand-blue); }
  .search-toggle { position: absolute; left: 1010px; top: 26px; width: 26px; height: 26px; border: 1.5px solid #888; border-radius: 50%; }

  .hero { position: absolute; top: 79px; left: 0; width: 1200px; height: 516px; }
  .hero-title { position: absolute; top: 280px; width: 100%; text-align: center; color: var(--white); font-family: "Open Sans", sans-serif; font-weight: 600; font-size: 45px; }
  .hero-subtitle { position: absolute; top: 337px; width: 100%; text-align: center; color: var(--white); font-family: "Open Sans", sans-serif; font-style: italic; font-size: 31px; }
  .hero-arrows { position: absolute; left: 583px; top: 548px; }

  .about { position: absolute; top: 595px; left: 0; width: 1200px; height: 503px; }
  .about-title { position: absolute; left: 164px; top: 62px; font-family: "Open Sans", sans-serif; font-weight: 600; font-size: 27px; color: var(--brand-blue); }
  .about-text { position: absolute; left: 161px; top: 118px; width: 370px; font-size: 14px; line-height: 24.5px; color: var(--ink); }
  .about-text p + p { margin-top: 24.5px; }

  .video { position: absolute; top: 1098px; left: 0; width: 1200px; height: 308px; }

  .services { position: absolute; top: 1415px; left: 0; width: 1200px; height: 426px; }
  .services-title { position: absolute; left: 161px; top: 198px; font-family: "Open Sans", sans-serif; font-weight: 600; font-size: 26px; color: var(--white); letter-spacing: 0.5px; }
  .service-label { position: absolute; color: var(--white); font-size: 15.5px; display: flex; align-items: center; gap: 10px; }

  .testimonials { position: absolute; top: 1880px; left: 0; width: 1200px; }
  .testimonials-title { text-align: center; font-family: "Open Sans", sans-serif; font-weight: 600; font-size: 29px; color: var(--brand-blue); margin-top: 25px; }
  .testimonial-quote { width: 720px; margin: 22px auto 0; text-align: center; font-size: 14px; line-height: 25.5px; color: var(--ink); }
  .quote-mark { color: var(--brand-blue); font-family: "Open Sans", sans-serif; font-weight: 700; font-size: 22px; line-height: 0; }
  .testimonial-author { text-align: center; margin-top: 14px; font-family: "Open Sans", sans-serif; font-weight: 600; font-size: 16px; color: var(--ink); }
  .testimonial-author .name { color: var(--brand-blue); }

  .site-footer { position: absolute; top: 2145px; left: 0; width: 1200px; height: 321px; background: linear-gradient(180deg, #1a5fae 0%, #0f57a8 55%, #0c4d98 100%); color: var(--white); }
  .footer-heading { position: absolute; font-family: "Open Sans", sans-serif; font-weight: 600; font-size: 15px; }
  .footer-text { position: absolute; font-size: 13px; line-height: 21.5px; }
  .quote-phone { position: absolute; left: 161px; top: 78px; font-size: 23px; }
  .social-dot { position: absolute; top: 160px; width: 26px; height: 26px; border: 1.3px solid var(--white); border-radius: 50%; }
  .copyright { position: absolute; top: 266px; width: 100%; text-align: center; font-size: 12px; }
</style>
</head>
<body>

<header class="site-header">
  <div class="brand"><span class="brand-mark"></span><span class="brand-name">HARWOOD HOMES</span></div>
  <nav class="main-nav">
    <a class="is-active" style="left:546px">HOME</a>
    <a style="left:630px">SERVICES</a>
    <a style="left:732px">ABOUT</a>
    <a style="left:816px">PROJECTS</a>
    <a style="left:922px">CONTACT</a>
  </nav>
  <span class="search-toggle"></span>
</header>

<section class="hero">
  <svg width="1200" height="516" style="position:absolute;top:0;left:0">
    <defs>
      <linearGradient id="heroA" x1="0" y1="0" x2="0" y2="1"><stop offset="0" stop-color="#4b5560"/><stop offset="1" stop-color="#2c3138"/></linearGradient>
      <linearGradient id="heroB" x1="0" y1="0" x2="1" y2="1"><stop offset="0" stop-color="#3a3633"/><stop offset="1" stop-color="#5a4a3c"/></linearGradient>
      <linearGradient id="heroC" x1="0" y1="0" x2="0" y2="1"><stop offset="0" stop-color="#3c4450"/><stop offset="1" stop-color="#24282d"/></linearGradient>
      <linearGradient id="heroD" x1="0" y1="0" x2="0" y2="1"><stop offset="0" stop-color="#505b67"/><stop offset="1" stop-color="#2a2c2f"/></linearGradient>
    </defs>
    <rect role="img" aria-label="Modern two-storey house with timber cladding" x="0" y="0" width="600" height="256" fill="url(#heroA)"/>
    <rect role="img" aria-label="Open-plan living room with staircase" x="600" y="0" width="600" height="256" fill="url(#heroB)"/>
    <rect role="img" aria-label="White weatherboard house with garage at dusk" x="0" y="256" width="600" height="260" fill="url(#heroC)"/>
    <rect role="img" aria-label="Gabled house with lit windows at dusk" x="600" y="256" width="600" height="260" fill="url(#heroD)"/>
  </svg>
  <h1 class="hero-title">Creating and Renovating</h1>
  <p class="hero-subtitle">Beautiful and Unusual Buildings</p>
  <svg class="hero-arrows" width="34" height="20" viewBox="0 0 34 20">
    <path d="M7 4 L1 10 L7 16 M27 4 L33 10 L27 16" stroke="#fff" stroke-width="2.5" fill="none"/>
    <circle cx="17" cy="10" r="5" stroke="#fff" stroke-width="2.5" fill="none"/>
  </svg>
</section>

<section class="about">
  <svg width="1200" height="503" style="position:absolute;top:0;left:0">
    <defs>
      <linearGradient id="aboutPhoto" x1="0" y1="0" x2="0" y2="1"><stop offset="0" stop-color="#a9c3de"/><stop offset="0.45" stop-color="#8a9097"/><stop offset="1" stop-color="#4f4c47"/></linearGradient>
    </defs>
    <polygon role="img" aria-label="House under construction wrapped in scaffolding with a work van" points="674,0 1200,0 1200,503 551,503" fill="url(#aboutPhoto)"/>
  </svg>
  <h2 class="about-title">About Harwood Homes</h2>
  <div class="about-text">
    <p>Harwood Homes is dedicated to creating and renovating beautiful and unusual buildings.</p>
    <p>Harwood Homes works with you to take dream houses off the blueprints and into reality. We have the knowledge and expertise to customise homes to suit you – from unusual materials and designs to environmentally<br>sensitive locations.</p>
    <p>Sed ut perspiciatis unde omnis iste natus error sit voluptat cusantium dSed ut perspiciatis unde omnis iste natus error voluptatem accusantium.</p>
  </div>
</section>

<section class="video">
  <svg width="1200" height="308" style="position:absolute;top:0;left:0">
    <defs>
      <linearGradient id="videoBg" x1="0" y1="0" x2="1" y2="0"><stop offset="0" stop-color="#4a4744"/><stop offset="0.5" stop-color="#6b6762"/><stop offset="1" stop-color="#3f3d3b"/></linearGradient>
    </defs>
    <rect role="img" aria-label="Interior hallway with white staircase and timber floor" width="1200" height="308" fill="url(#videoBg)"/>
    <circle cx="600" cy="155" r="35" fill="none" stroke="#fff" stroke-width="4"/>
    <polygon points="590,137 590,173 619,155" fill="#fff"/>
  </svg>
</section>

<section class="services">
  <svg width="1200" height="426" style="position:absolute;top:0;left:0">
    <defs>
      <linearGradient id="svcMain" x1="0" y1="0" x2="0" y2="1"><stop offset="0" stop-color="#6f7f8c"/><stop offset="0.6" stop-color="#4a4a46"/><stop offset="1" stop-color="#3a4a2e"/></linearGradient>
      <linearGradient id="svcPlan" x1="0" y1="0" x2="0" y2="1"><stop offset="0" stop-color="#8c8a86"/><stop offset="1" stop-color="#3a3a3a"/></linearGradient>
      <linearGradient id="svcModel" x1="0" y1="0" x2="0" y2="1"><stop offset="0" stop-color="#d8dde3"/><stop offset="1" stop-color="#8a4a34"/></linearGradient>
      <linearGradient id="svcManage" x1="0" y1="0" x2="0" y2="1"><stop offset="0" stop-color="#9aa0a4"/><stop offset="1" stop-color="#4a4a3e"/></linearGradient>
    </defs>
    <polygon role="img" aria-label="Modern house lit at dusk" points="0,0 608,0 493,426 0,426" fill="url(#svcMain)"/>
    <polygon role="img" aria-label="Hands reviewing construction plans" points="616,0 962,0 906,195 563,195" fill="url(#svcPlan)"/>
    <polygon role="img" aria-label="Model house on building plans with bricks" points="560,205 903,205 847,426 501,426" fill="url(#svcModel)"/>
    <polygon role="img" aria-label="Site managers in hard hats" points="970,0 1200,0 1200,426 855,426" fill="url(#svcManage)"/>
  </svg>
  <h2 class="services-title">OUR SERVICES</h2>
  <div class="service-label" style="left:594px;top:158px">
    <svg width="24" height="24" viewBox="0 0 24 24"><rect x="3" y="4" width="15" height="18" fill="none" stroke="#fff" stroke-width="2"/><path d="M7 10h7M7 14h5M14 18 L22 6" stroke="#fff" stroke-width="2"/></svg>
    Preconstruction Planning
  </div>
  <div class="service-label" style="left:526px;top:387px">
    <svg width="22" height="22" viewBox="0 0 24 24"><path d="M12 2 L22 7 L22 17 L12 22 L2 17 L2 7 Z M2 7 L12 12 L22 7 M12 12 L12 22" fill="none" stroke="#fff" stroke-width="2"/></svg>
    Construction Modelling
  </div>
  <div class="service-label" style="left:890px;top:385px">
    <svg width="24" height="26" viewBox="0 0 24 26"><path d="M5 9 Q12 0 19 9 Z" fill="#fff"/><rect x="8" y="10" width="8" height="6" fill="#fff"/><path d="M3 26 Q3 18 12 18 Q21 18 21 26 Z" fill="#fff"/></svg>
    Full Project Management
  </div>
</section>

<section class="testimonials">
  <h2 class="testimonials-title">Client Testimonials</h2>
  <p class="testimonial-quote"><span class="quote-mark">“</span> Sed ut perspiciatis unde omnis iste natus error sit voluptatem accusantium doloremque laudantium, totam rm aperiam, eaque ipsa quaeinventore veritatis et quasi architecto beatae vitae dicta sunt explicabomo enim ipsam votatem quia voluptas sit aspernatur aut odit aut fugised quia consequuntur magni dolores eos qui ratione voluptate nesciunteque porro quisquam est, qui dolorem ipsum quia dolor sit ametconsectetur, adipeli. <span class="quote-mark">”</span></p>
  <p class="testimonial-author"><span class="name">Mara Ellis</span>, City Name</p>
</section>

<footer class="site-footer">
  <svg width="1200" height="321" style="position:absolute;top:0;left:0">
    <line x1="424" y1="47" x2="378" y2="193" stroke="rgba(255,255,255,0.45)" stroke-width="1"/>
    <line x1="748" y1="47" x2="702" y2="193" stroke="rgba(255,255,255,0.45)" stroke-width="1"/>
  </svg>
  <h3 class="footer-heading" style="left:161px;top:48px">Get a quote:</h3>
  <p class="quote-phone">09 555 0142</p>
  <h3 class="footer-heading" style="left:161px;top:128px;font-size:14px">Follow Us</h3>
  <span class="social-dot" style="left:160px"></span>
  <span class="social-dot" style="left:191px"></span>
  <span class="social-dot" style="left:222px"></span>
  <span class="social-dot" style="left:253px"></span>

  <h3 class="footer-heading" style="left:506px;top:45px">Head Office</h3>
  <p class="footer-text" style="left:506px;top:86px">18 Larchmont Road,<br>Flat Bush Auckland</p>
  <p class="footer-text" style="left:506px;top:150px">info@harwoodhomes.co.nz<br>Tel: 0064 9 555 0142</p>

  <h3 class="footer-heading" style="left:814px;top:45px">Employment</h3>
  <p class="footer-text" style="left:814px;top:86px;width:240px">To apply for a job with Harwood Homes, please send a cover letter together with your C.V. to: info@harwoodhomes.co.nz</p>

  <p class="copyright">© 2017 Harwood Homes. All Copyrights are Reserved · Terms · Privacy</p>
</footer>

</body>
</html>
```